" A Velmar iniciou suas atividades em Vila Serena há cerca de 30 dias. Atualmente funciona com um consultório de atendimento médico montado dentro de uma clínica maior, chamada Nefrovita. O objetivo ao longo do tempo é ocupar um espaço cada vez maior tornando uma clínica propriamente dita, com métodos diagnósticos agregados, porém, sempre no mesmo conceito de divisao de espaço com a Nefrovita. Assim, o primeiro passo é montar uma identidade própria, e tudo começa com a criaçao do logo e dos materiais de identidade, tal como receituários, papel timbrado, pastas, envelopes. "

```html
<!DOCTYPE html>
<html lang="pt-BR">
<head>
<meta charset="utf-8">
<title>Velmar — Papelaria</title>
<link rel="stylesheet" href="https://fonts.googleapis.com/css2?family=Roboto:wght@400;700&display=swap">
<style>
  :root {
    --page: #ffffff;
    --board: #353230;
    --paper: #ffffff;
    --red: #b11a22;
    --red-dark: #7d0d14;
    --red-light: #d0323a;
    --ink: #3a3a3a;
    --ink-soft: #8a8a8a;
    --on-red: #f4dada;
  }
  * { box-sizing: border-box; margin: 0; padding: 0; }
  html, body { width: 1200px; height: 1200px; overflow: hidden; }
  body {
    background: var(--page);
    font-family: "Roboto", Arial, sans-serif;
    position: relative;
  }
  .board {
    position: absolute; left: 0; top: 199px;
    width: 1200px; height: 804px;
    background: var(--board);
  }
  .piece { position: absolute; overflow: hidden; }
  .red-field {
    background: radial-gradient(ellipse at 50% 40%, var(--red-light) 0%, var(--red) 45%, var(--red-dark) 100%);
  }
  .white-field { background: var(--paper); }

  .brand {
    display: flex; align-items: center; gap: 6px;
    font-weight: 700; color: var(--ink); line-height: 1;
  }
  .brand .dot { border-radius: 50%; background: var(--red); flex: none; }
  .brand.on-red { color: var(--paper); }
  .brand.on-red .dot { background: var(--paper); }
  .tagline { font-size: 6px; color: var(--ink-soft); letter-spacing: .5px; margin-top: 3px; }

  .small-lines { font-size: 6px; line-height: 1.5; color: var(--on-red); }

  /* folder */
  .folder { left: 271px; top: 288px; width: 411px; height: 264px; display: flex; }
  .folder .cover { width: 200px; height: 100%; position: relative; }
  .folder .inside { flex: 1; display: flex; align-items: center; justify-content: center; }
  .folder .cover-footer { position: absolute; left: 106px; bottom: 14px; }

  /* business cards */
  .card-front { left: 686px; top: 295px; width: 245px; height: 130px; border-top-right-radius: 28px;
    display: flex; align-items: center; justify-content: center; }
  .card-back { left: 686px; top: 439px; width: 245px; height: 135px; }
  .card-back .contact { position: absolute; left: 142px; top: 16px; }
  .card-back .contact p { margin-bottom: 8px; }
  .card-back .brand { position: absolute; right: 10px; bottom: 10px; font-size: 11px; }

  /* envelopes */
  .envelope-white { left: 336px; top: 571px; width: 144px; height: 300px;
    display: flex; align-items: center; justify-content: center; }
  .envelope-white .flap { position: absolute; left: 0; top: 0; width: 100%; height: 22px; }
  .envelope-red { left: 504px; top: 600px; width: 204px; height: 276px; }
  .envelope-red .footer { position: absolute; left: 0; right: 0; bottom: 14px; text-align: center; }
  .envelope-red .footer .brand { justify-content: center; font-size: 12px; }
</style>
</head>
<body>
  <div class="board"></div>

  <!-- Folder -->
  <section class="piece folder">
    <div class="cover red-field" role="img" aria-label="Large heart outline with heartbeat line on red background">
      <div class="cover-footer">
        <div class="brand on-red" style="font-size:11px"><span class="dot" style="width:7px;height:7px"></span>Velmar</div>
        <div class="small-lines" style="margin-top:3px">Rua Central 120, Centro<br>Vila Serena</div>
      </div>
    </div>
    <div class="inside white-field">
      <div>
        <div class="brand" style="font-size:20px"><span class="dot" style="width:12px;height:12px"></span>Velmar</div>
        <div class="tagline">clínica do coração</div>
      </div>
    </div>
  </section>

  <!-- Business card, front -->
  <section class="piece card-front white-field">
    <div>
      <div class="brand" style="font-size:16px"><span class="dot" style="width:10px;height:10px"></span>Velmar</div>
      <div class="tagline">clínica do coração</div>
    </div>
  </section>

  <!-- Business card, back -->
  <section class="piece card-back red-field" role="img" aria-label="Heart outline with heartbeat line on red background">
    <div class="contact small-lines">
      <p>Dr. Ana Lima<br>Cardiologia</p>
      <p>contato@velmar.med<br>(90) 3300-0000</p>
      <p>Rua Central 120<br>Vila Serena</p>
    </div>
    <div class="brand on-red"><span class="dot" style="width:7px;height:7px"></span>Velmar</div>
  </section>

  <!-- Envelope, white -->
  <section class="piece envelope-white white-field">
    <svg class="flap" viewBox="0 0 144 22" preserveAspectRatio="none">
      <polyline points="0,0 8,20 136,20 144,0" fill="none" stroke="#d8d8d8" stroke-width="1"/>
    </svg>
    <div>
      <div class="brand" style="font-size:15px"><span class="dot" style="width:9px;height:9px"></span>Velmar</div>
      <div class="tagline">clínica do coração</div>
    </div>
  </section>

  <!-- Envelope, red -->
  <section class="piece envelope-red red-field" role="img" aria-label="Large heart outline with heartbeat line on red background">
    <div class="footer">
      <div class="brand on-red"><span class="dot" style="width:7px;height:7px"></span>Velmar</div>
      <div class="small-lines" style="margin-top:3px">Rua Central 120<br>Vila Serena</div>
    </div>
  </section>
</body>
</html>
```